Law firm needs stationary and envelope design*

We would like to incorporate our logo into letterhead design and envelopes. We are looking for something that is moderately conservative but not old law firm style. Both the envelopes and the letterhead must have both firm addresses. We would like to incorporate the color of the logo, but only a small amount of color - perhaps on one of the borders. The addresses for the firm locations are listed below. Given that it is a law firm, it needs to somewhat conservative, but not the old school, small black font on cream colored paper design.

The firm addresses are:

27815 N. Harlow Pemberton Pkwy.
Ste 740
Scottsdale, AZ 85419

6208 E. Juniper Street
Ste 820
Burbank, CA 91873

Legal

Designer to choose colors to be used in the design.

• Both addresses:
• 27815 N. Harlow Pemberton Pkwy.
• Ste 740
• Scottsdale, AZ 85419
• 6208 E. Juniper Street
• Ste 820
• Burbank, CA 91873
• Small amount of color on border(s) that matches the logo but not too much color

```html
<!DOCTYPE html>
<html lang="en">
<head>
<meta charset="utf-8">
<title>Halvern Law – Letterhead and Envelope</title>
<link rel="stylesheet" href="https://fonts.googleapis.com/css2?family=Marcellus&family=Arimo:wght@400&display=swap">
<style>
  :root {
    --ink: #464a91;
    --paper: #ffffff;
    --backdrop: #e9e9ec;
    --shade: rgba(0,0,0,0.14);
  }
  html, body {
    margin: 0;
    padding: 0;
    overflow: hidden;
  }
  body {
    width: 960px;
    height: 1200px;
    background: var(--backdrop);
    position: relative;
  }
  .sheet {
    position: absolute;
    background: var(--paper);
    box-shadow: 0 4px 14px var(--shade);
  }
  .letterhead { left: 200px; top: 28px; width: 560px; height: 725px; }
  .envelope   { left: 40px; top: 790px; width: 880px; height: 382px; }
  .sheet svg { display: block; width: 100%; height: 100%; }
  .firm-name {
    font-family: "Marcellus", serif;
    fill: var(--ink);
    letter-spacing: 1px;
  }
  .address {
    font-family: "Arimo", Arial, sans-serif;
    fill: var(--ink);
  }
  .rule { stroke: var(--ink); fill: none; }
  .band { fill: var(--ink); }
</style>
</head>
<body>

<section class="sheet letterhead" aria-label="Letterhead">
  <svg viewBox="0 0 850 1100" xmlns="http://www.w3.org/2000/svg">
    <!-- frame -->
    <polyline class="rule" stroke-width="5" points="400,95 52,95 52,905 850,905"/>
    <polyline class="rule" stroke-width="2.5" points="400,110 66,110 66,891 850,891"/>
    <!-- firm name -->
    <text class="firm-name" x="797" y="118" font-size="58" text-anchor="end">HALVERN LAW</text>
    <!-- footer rules -->
    <line class="rule" x1="0" y1="924" x2="295" y2="924" stroke-width="0.8"/>
    <line class="rule" x1="0" y1="937" x2="295" y2="937" stroke-width="1.6"/>
    <line class="rule" x1="0" y1="954" x2="295" y2="954" stroke-width="2.8"/>
    <line class="rule" x1="0" y1="973" x2="295" y2="973" stroke-width="5.5"/>
    <!-- addresses -->
    <g class="address" font-size="17">
      <text x="312" y="944">27815 N. Harlow Pemberton Pkwy.</text>
      <text x="312" y="968">Ste 740</text>
      <text x="312" y="992">Scottsdale, AZ 85419</text>
      <text x="820" y="956" text-anchor="end">6208 E. Juniper Street</text>
      <text x="820" y="980" text-anchor="end">Ste 820</text>
      <text x="820" y="1004" text-anchor="end">Burbank, CA 91873</text>
    </g>
    <line class="rule" x1="600" y1="930" x2="600" y2="1002" stroke-width="1"/>
    <!-- base band -->
    <rect class="band" x="0" y="1078" width="850" height="22"/>
  </svg>
</section>

<section class="sheet envelope" aria-label="Envelope">
  <svg viewBox="0 0 950 412" xmlns="http://www.w3.org/2000/svg">
    <!-- firm name -->
    <text class="firm-name" x="95" y="150" font-size="56">HALVERN LAW</text>
    <!-- frame -->
    <polyline class="rule" stroke-width="5" points="590,95 890,95 890,345 790,345"/>
    <polyline class="rule" stroke-width="1.8" points="598,112 874,112 874,329 790,329"/>
    <!-- left rules -->
    <line class="rule" x1="130" y1="318" x2="560" y2="318" stroke-width="0.8"/>
    <line class="rule" x1="130" y1="333" x2="560" y2="333" stroke-width="1.6"/>
    <line class="rule" x1="130" y1="350" x2="560" y2="350" stroke-width="3"/>
    <line class="rule" x1="130" y1="370" x2="560" y2="370" stroke-width="8"/>
    <!-- addresses -->
    <g class="address" font-size="18">
      <text x="556" y="248" text-anchor="end">27815 N. Harlow Pemberton Pkwy.</text>
      <text x="556" y="273" text-anchor="end">Ste 740</text>
      <text x="556" y="298" text-anchor="end">Scottsdale, AZ 85419</text>
      <text x="576" y="310">6208 E. Juniper Street</text>
      <text x="576" y="335">Ste 820</text>
      <text x="576" y="360">Burbank, CA 91873</text>
    </g>
  </svg>
</section>

</body>
</html>
```